Mondaxe custom business card design

Need a authentic, innovative business card design for a new mobile app business. I am uploading a few screen images from our app for you to view. I would like app design theme to match business card design. I can also send logo images.

```html
<!DOCTYPE html>
<html lang="en">
<head>
<meta charset="utf-8">
<title>Mondaxe business card</title>
<link rel="stylesheet" href="https://fonts.googleapis.com/css2?family=Montserrat:wght@400;500;700;800&display=swap">
<style>
  :root {
    --bg: #ecebe8;
    --ink: #141414;
    --card-dark: #000000;
    --card-light: #ffffff;
    --purple: #4a0a86;
    --white: #ffffff;
  }
  * { margin: 0; padding: 0; box-sizing: border-box; }
  html, body { width: 1200px; height: 773px; overflow: hidden; }
  body {
    background: var(--bg);
    font-family: "Montserrat", Arial, sans-serif;
    color: var(--ink);
    position: relative;
  }
  .card {
    position: absolute;
    top: 236px;
    width: 500px;
    height: 300px;
    border-radius: 18px;
    overflow: hidden;
    box-shadow: 0 8px 24px rgba(0,0,0,0.18);
  }
  .card-back {
    left: 70px;
    background: var(--card-dark);
    display: flex;
    align-items: center;
    justify-content: center;
  }
  .brand-lockup {
    display: flex;
    align-items: center;
    gap: 14px;
  }
  .brand-dot {
    width: 34px; height: 34px;
    border-radius: 50%;
    background: var(--purple);
  }
  .brand-name-back {
    font-weight: 800;
    font-size: 40px;
    color: var(--white);
    letter-spacing: -0.5px;
  }
  .card-front {
    left: 630px;
    background: var(--card-light);
  }
  .accent-circle {
    position: absolute;
    right: -70px;
    top: -40px;
    width: 270px;
    height: 270px;
    border-radius: 50%;
    background: var(--purple);
  }
  .brand-name-front {
    position: absolute;
    left: 30px;
    top: 48px;
    font-weight: 800;
    font-size: 30px;
    color: var(--ink);
    letter-spacing: -0.5px;
  }
  .person {
    position: absolute;
    left: 30px;
    top: 150px;
  }
  .person-name { font-weight: 700; font-size: 19px; }
  .person-role { font-weight: 500; font-size: 11px; margin-top: 2px; }
  .contact-list {
    position: absolute;
    left: 30px;
    top: 200px;
    list-style: none;
    font-size: 11px;
    font-weight: 500;
  }
  .contact-list li {
    display: flex;
    align-items: center;
    gap: 8px;
    height: 17px;
  }
  .contact-list svg { width: 12px; height: 12px; flex: none; }
  .contact-list .address { padding-left: 20px; margin-top: 4px; }
</style>
</head>
<body>
  <section class="card card-back">
    <div class="brand-lockup">
      <span class="brand-dot"></span>
      <span class="brand-name-back">Mondaxe</span>
    </div>
  </section>

  <section class="card card-front">
    <div class="accent-circle"></div>
    <div class="brand-name-front">Mondaxe</div>
    <div class="person">
      <div class="person-name">Rory Callister</div>
      <div class="person-role">Founder &amp; CEO</div>
    </div>
    <ul class="contact-list">
      <li>
        <svg viewBox="0 0 24 24" fill="none" stroke="#4a0a86" stroke-width="2"><path d="M5 3h4l2 5-3 2a11 11 0 0 0 6 6l2-3 5 2v4a2 2 0 0 1-2 2A17 17 0 0 1 3 5a2 2 0 0 1 2-2z"/></svg>
        +34 611 205 947
      </li>
      <li>
        <svg viewBox="0 0 24 24" fill="none" stroke="#4a0a86" stroke-width="2"><rect x="3" y="5" width="18" height="14" rx="1"/><path d="M3 6l9 7 9-7"/></svg>
        rory@mondaxeapp.com
      </li>
      <li>
        <svg viewBox="0 0 24 24" fill="none" stroke="#4a0a86" stroke-width="2"><circle cx="12" cy="12" r="9"/><path d="M3 12h18M12 3c3 3 3 15 0 18M12 3c-3 3-3 15 0 18"/></svg>
        www.mondaxeapp.com
      </li>
      <li class="address">48 Harbor Lane, Portland, OR 9721</li>
    </ul>
  </section>
</body>
</html>
```